Business Card Design Project

I have attached the logo and the colour pallete for the branding for the company.

Creative designs for business cards are needed.

The Company is modern corporate.

Industry/Entity Type

Business

```html
<!DOCTYPE html>
<html lang="en">
<head>
<meta charset="utf-8">
<title>Tenvia Business Card</title>
<link href="https://fonts.googleapis.com/css2?family=Exo+2:wght@600;700&family=Jost:wght@400;500&display=swap" rel="stylesheet">
<style>
  :root {
    --purple: #4a1a50;
    --purple-deep: #32103a;
    --purple-light: #55215c;
    --orange: #e8672a;
    --paper: #f4f3f0;
    --backdrop: #d6dadb;
    --ink: #3b1a40;
  }
  * { margin: 0; padding: 0; box-sizing: border-box; }
  html, body { width: 1200px; height: 960px; overflow: hidden; }
  body {
    background: var(--backdrop);
    position: relative;
    font-family: "Jost", sans-serif;
  }
  .card {
    position: absolute;
    left: 280px;
    width: 640px;
    height: 366px;
    border-radius: 3px;
    overflow: hidden;
    box-shadow: 0 6px 18px rgba(40, 40, 50, 0.18);
  }
  /* Back side */
  .card-back {
    top: 70px;
    background: linear-gradient(135deg, var(--purple-deep) 0%, var(--purple-light) 100%);
  }
  .card-back .brand-name {
    position: absolute;
    right: 40px;
    bottom: 30px;
    color: #ffffff;
    font-family: "Exo 2", sans-serif;
    font-weight: 700;
    font-size: 36px;
    letter-spacing: 0.5px;
  }
  /* Front side */
  .card-front {
    top: 520px;
    background: var(--paper);
  }
  .card-front .brand-name {
    position: absolute;
    left: 56px;
    top: 34px;
    color: var(--purple);
    font-family: "Exo 2", sans-serif;
    font-weight: 700;
    font-size: 34px;
    letter-spacing: 0.5px;
  }
  .holder {
    position: absolute;
    right: 50px;
    top: 96px;
    text-align: right;
  }
  .holder-name {
    font-family: "Exo 2", sans-serif;
    font-weight: 700;
    font-size: 28px;
    color: var(--purple-deep);
    line-height: 1;
  }
  .holder-title {
    font-size: 15px;
    color: var(--purple);
    margin-top: 4px;
  }
  .side-tab {
    position: absolute;
    left: 0;
    top: 140px;
    width: 26px;
    height: 82px;
    background: var(--orange);
  }
  .contacts {
    position: absolute;
    left: 64px;
    top: 150px;
    list-style: none;
    font-size: 10.5px;
    color: var(--ink);
    line-height: 1.35;
  }
  .contacts li {
    display: flex;
    align-items: flex-start;
    gap: 12px;
    margin-bottom: 8px;
  }
  .contacts svg { flex: none; width: 12px; height: 12px; margin-top: 1px; }
  .footer-bands {
    position: absolute;
    left: 0;
    bottom: 0;
    width: 640px;
    height: 40px;
  }
  .website {
    position: absolute;
    right: 30px;
    bottom: 8px;
    color: #ffffff;
    font-size: 16px;
    font-weight: 500;
    letter-spacing: 0.6px;
  }
</style>
</head>
<body>

  <section class="card card-back" aria-label="Card back">
    <div class="brand-name">tenvia</div>
  </section>

  <section class="card card-front" aria-label="Card front">
    <div class="brand-name">tenvia</div>

    <div class="holder">
      <div class="holder-name">Your Name</div>
      <div class="holder-title">Title</div>
    </div>

    <div class="side-tab"></div>

    <ul class="contacts">
      <li>
        <svg viewBox="0 0 12 12" aria-hidden="true"><path d="M6 0.5a4 4 0 0 0-4 4c0 3 4 7 4 7s4-4 4-7a4 4 0 0 0-4-4z" fill="var(--orange)"/><circle cx="6" cy="4.5" r="1.5" fill="var(--paper)"/></svg>
        <span>Address , Street no 1234 , Quarter no 1234<br>City ,State , Country , PIN no 123456</span>
      </li>
      <li>
        <svg viewBox="0 0 12 12" aria-hidden="true"><circle cx="6" cy="6" r="5.2" fill="none" stroke="var(--orange)" stroke-width="1.2"/><path d="M4.2 3.4l1 .1.5 1.4-.7.6c.3.8.8 1.3 1.5 1.6l.6-.7 1.4.5.1 1c-.3.5-.9.7-1.5.6-1.9-.4-3.2-1.8-3.5-3.7-.1-.6.1-1.1.6-1.4z" fill="var(--orange)"/></svg>
        <span>011-123-4567</span>
      </li>
      <li>
        <svg viewBox="0 0 12 12" aria-hidden="true"><rect x="0.5" y="2" width="11" height="8" fill="var(--orange)" opacity="0.75"/><path d="M0.5 2l5.5 4.5L11.5 2" fill="none" stroke="var(--paper)" stroke-width="1"/></svg>
        <span>emailaddress@website.com</span>
      </li>
    </ul>

    <svg class="footer-bands" viewBox="0 0 640 40" aria-hidden="true">
      <polygon points="0,10 380,10 390,40 0,40" fill="var(--purple)"/>
      <polygon points="388,0 640,0 640,40 400,40" fill="var(--orange)"/>
    </svg>
    <div class="website">Yourwebsite.com</div>
  </section>

</body>
</html>
```